Makeup Artist Requires Business Card design

Hi

I am looking for a business card design to market my makeup artist business. I operate under my own name Mara Veldt and I would like to keep the design of the card very simplistic and chic - something that keeps both my name and profession (makeup artist) the focus of the card. I would like it to be a style that is eyecatching to the reader (i am open to anything unusual) but upmarket.

Target Market(s)

women, magazine/beauty/fashion editors, photographers.

Industry/Entity Type

Business

Requirements
Must have
• Must contain:

Phone number: 0418 372 915
Website: www.maraveldt.com.au
email: contact@maraveldt.com.au

(although you don't need to have prefaced these with the words phone number, website etc :))
Should not have
• I am not looking for anything overly colorful - my preference is to keep the card dark if possible.

```html
<!DOCTYPE html>
<html lang="en">
<head>
<meta charset="utf-8">
<title>Mara Veldt – Makeup Artist Business Card</title>
<link rel="stylesheet" href="https://fonts.googleapis.com/css2?family=Pinyon+Script&family=Montserrat:wght@300;400&display=swap">
<style>
  :root {
    --backdrop: #262626;
    --card: #1b1b1b;
    --card-edge: #2a2a2a;
    --ink-script: #9a9a9a;
    --ink-text: #8c8c8c;
    --ink-soft: #7a7a7a;
  }
  * { margin: 0; padding: 0; box-sizing: border-box; }
  html, body {
    width: 1200px;
    height: 901px;
    overflow: hidden;
    background: var(--backdrop);
  }
  .canvas {
    width: 1200px;
    height: 901px;
    display: flex;
    align-items: center;
    justify-content: center;
    gap: 60px;
  }
  .card {
    width: 520px;
    height: 318px;
    background: var(--card);
    border: 1px solid var(--card-edge);
    border-radius: 24px;
    position: relative;
    box-shadow: 0 18px 40px rgba(0,0,0,0.45);
  }
  .card-front .brand {
    position: absolute;
    left: 50%;
    top: 50%;
    transform: translate(-50%, -58%);
    text-align: right;
  }
  .brand-name {
    font-family: "Pinyon Script", cursive;
    font-size: 78px;
    line-height: 1;
    color: var(--ink-script);
    white-space: nowrap;
  }
  .brand-role {
    font-family: "Montserrat", sans-serif;
    font-weight: 300;
    font-size: 19px;
    letter-spacing: 1px;
    color: var(--ink-soft);
    margin-top: 2px;
    margin-right: 6px;
  }
  .card-back .details {
    position: absolute;
    left: 0;
    right: 0;
    top: 96px;
    text-align: center;
    font-family: "Montserrat", sans-serif;
    font-weight: 300;
    color: var(--ink-text);
  }
  .details .name { font-size: 17px; letter-spacing: 0.5px; }
  .details .role { font-size: 12px; color: var(--ink-soft); margin-top: 3px; }
  .details .contact { margin-top: 38px; font-size: 13px; line-height: 1.55; }
</style>
</head>
<body>
  <main class="canvas">
    <section class="card card-front" aria-label="Card front">
      <div class="brand">
        <div class="brand-name">Mara Veldt</div>
        <div class="brand-role">Makeup Artist</div>
      </div>
    </section>
    <section class="card card-back" aria-label="Card back">
      <div class="details">
        <div class="name">Mara Veldt</div>
        <div class="role">Makeup Artist</div>
        <div class="contact">
          <div class="phone">0418 372 915</div>
          <div class="email">contact@maraveldt.com.au</div>
          <div class="web">www.maraveldt.com.au</div>
        </div>
      </div>
    </section>
  </main>
</body>
</html>
```